BRENSDALE ELECTRICAL

all black background with silver and lime writing, fonts i like are gothic style but am open to ideas, will need a picture logo aswell as im putting this on my van.i am a electrical contractor starting up my own electrical business. underneath brensdale electrical heading on card we could put" professiona cost effective soloutions to all your electrical needs".{ or something of that nature }.on aback of card on top half list servises provided, real estate and commercial maintenance, new home and renovation rewires and upgrades, split system air conditioning, floor heat, tv phone data, smoke detoctors, lighting systems , builders welcome, , and also a thankyou for your business.

Real Estate

GERALD PILWORTHY
brensdaleelectrical@mailvox.com.au
0417302951
lic no 58120
ac lic no l293417
abn 37216058814

```html
<!DOCTYPE html>
<html lang="en">
<head>
<meta charset="utf-8">
<title>Brensdale Electrical – Business Cards</title>
<link rel="stylesheet" href="https://fonts.googleapis.com/css2?family=Exo+2:wght@600&family=Arimo:wght@400;700&family=Noto+Sans&display=swap">
<style>
  :root {
    --page: #e6e4e1;
    --card-black: #000000;
    --panel-blue: #2b2f7c;
    --panel-blue-light: #5a5aa8;
    --line-purple: #4b48a0;
    --hot-red: #e31e25;
    --hot-orange: #f7941d;
    --hot-yellow: #fdc010;
    --cool-purple: #7a6fb0;
    --cool-navy: #2a2d7a;
    --silver-light: #ffffff;
    --silver-dark: #9a9a9a;
    --lime: #6cc04a;
    --white: #ffffff;
  }
  html, body {
    margin: 0;
    width: 1200px;
    height: 1200px;
    overflow: hidden;
    background: var(--page);
  }
  .sheet {
    width: 1200px;
    height: 1200px;
    display: flex;
    flex-direction: column;
    align-items: center;
    justify-content: center;
    gap: 17px;
  }
  .card {
    display: block;
    width: 926px;
    height: 573px;
    box-shadow: 0 6px 14px rgba(0,0,0,0.35);
  }
  .brand-title { font-family: "Exo 2", sans-serif; font-weight: 600; letter-spacing: 1px; }
  .tagline { font-family: "Noto Sans", sans-serif; fill: var(--lime); }
  .person-name { font-family: "Arimo", sans-serif; font-weight: 700; fill: #e8e8f4; }
  .person-role, .contact-text { font-family: "Arimo", sans-serif; fill: var(--white); }
  .mark-name { font-family: "Exo 2", sans-serif; font-weight: 600; fill: #d9d9d9; }
</style>
</head>
<body>
<main class="sheet">

  <!-- Front card -->
  <svg class="card card--front" viewBox="0 0 772 478" xmlns="http://www.w3.org/2000/svg">
    <defs>
      <linearGradient id="stripeHot" x1="0" x2="1">
        <stop offset="0" stop-color="var(--hot-red)"/>
        <stop offset="0.55" stop-color="var(--hot-orange)"/>
        <stop offset="1" stop-color="var(--hot-yellow)"/>
      </linearGradient>
      <linearGradient id="stripeCool" x1="0" x2="1">
        <stop offset="0" stop-color="var(--cool-purple)"/>
        <stop offset="1" stop-color="var(--cool-navy)"/>
      </linearGradient>
      <linearGradient id="stripeCoolRev" x1="0" x2="1">
        <stop offset="0" stop-color="var(--cool-navy)"/>
        <stop offset="1" stop-color="var(--cool-purple)"/>
      </linearGradient>
      <linearGradient id="stripeHotRev" x1="0" x2="1">
        <stop offset="0" stop-color="var(--hot-yellow)"/>
        <stop offset="0.45" stop-color="var(--hot-orange)"/>
        <stop offset="1" stop-color="var(--hot-red)"/>
      </linearGradient>
      <linearGradient id="silver" x1="0" y1="0" x2="0" y2="1">
        <stop offset="0" stop-color="var(--silver-light)"/>
        <stop offset="1" stop-color="var(--silver-dark)"/>
      </linearGradient>
      <radialGradient id="panelGlow" cx="0.55" cy="1" r="0.6">
        <stop offset="0" stop-color="var(--panel-blue-light)"/>
        <stop offset="1" stop-color="var(--panel-blue)"/>
      </radialGradient>
    </defs>

    <rect class="card-base" width="772" height="478" fill="var(--card-black)"/>
    <rect class="stripe" x="0" y="0" width="377" height="22" fill="url(#stripeHot)"/>
    <rect class="stripe" x="377" y="0" width="395" height="22" fill="url(#stripeCool)"/>

    <g class="brand-mark">
      <circle cx="121" cy="150" r="82" fill="none" stroke="#d9d9d9" stroke-width="4"/>
      <text class="mark-name" x="121" y="157" font-size="18" text-anchor="middle">BRENSDALE</text>
    </g>

    <text class="brand-title" x="235" y="132" font-size="40" fill="url(#silver)">BRENSDALE ELECTRICAL</text>
    <text class="tagline" x="235" y="160" font-size="21">professiona cost effective soloutions</text>
    <text class="tagline" x="235" y="187" font-size="21">to all your electrical needs</text>

    <rect class="divider-line" x="0" y="271" width="772" height="3" fill="var(--line-purple)"/>
    <rect class="contact-panel" x="0" y="278" width="772" height="170" fill="url(#panelGlow)"/>

    <text class="person-name" x="45" y="362" font-size="18">GERALD PILWORTHY</text>
    <text class="person-role" x="45" y="388" font-size="16">electrical contractor</text>

    <line class="panel-divider" x1="385" y1="293" x2="385" y2="440" stroke="var(--white)" stroke-width="1.5"/>

    <g class="contact-list">
      <text class="contact-text" x="413" y="321" font-size="16">@</text>
      <text class="contact-text" x="438" y="321" font-size="16.5">brensdaleelectrical@mailvox.com.au</text>
      <g class="icon-phone">
        <circle cx="421" cy="343" r="8" fill="var(--white)"/>
        <path d="M417 338 l2 -1 l2 3 l-1.5 1.2 q1 2.5 3.5 3.5 l1.2 -1.5 l3 2 l-1 2 q-7 0 -9.2 -9.2z" fill="var(--panel-blue)"/>
      </g>
      <text class="contact-text" x="438" y="349" font-size="16.5">0417302951</text>
      <text class="contact-text" x="413" y="391" font-size="16.5">lic no 58120 | Ac lic no l293417</text>
      <text class="contact-text" x="413" y="419" font-size="16.5">Abn 37216058814</text>
    </g>

    <rect class="stripe" x="0" y="455" width="387" height="23" fill="url(#stripeCoolRev)"/>
    <rect class="stripe" x="387" y="455" width="385" height="23" fill="url(#stripeHotRev)"/>
  </svg>

  <!-- Back card -->
  <svg class="card card--back" viewBox="0 0 772 478" xmlns="http://www.w3.org/2000/svg">
    <defs>
      <linearGradient id="bStripeHot" x1="0" x2="1">
        <stop offset="0" stop-color="var(--hot-red)"/>
        <stop offset="0.55" stop-color="var(--hot-orange)"/>
        <stop offset="1" stop-color="var(--hot-yellow)"/>
      </linearGradient>
      <linearGradient id="bStripeCool" x1="0" x2="1">
        <stop offset="0" stop-color="var(--cool-purple)"/>
        <stop offset="1" stop-color="var(--cool-navy)"/>
      </linearGradient>
      <linearGradient id="bStripeCoolRev" x1="0" x2="1">
        <stop offset="0" stop-color="var(--cool-navy)"/>
        <stop offset="1" stop-color="var(--cool-purple)"/>
      </linearGradient>
      <linearGradient id="bStripeHotRev" x1="0" x2="1">
        <stop offset="0" stop-color="var(--hot-yellow)"/>
        <stop offset="0.45" stop-color="var(--hot-orange)"/>
        <stop offset="1" stop-color="var(--hot-red)"/>
      </linearGradient>
      <linearGradient id="bSilver" x1="0" y1="0" x2="0" y2="1">
        <stop offset="0" stop-color="var(--silver-light)"/>
        <stop offset="1" stop-color="var(--silver-dark)"/>
      </linearGradient>
    </defs>

    <rect class="card-base" width="772" height="478" fill="var(--card-black)"/>
    <rect class="stripe" x="0" y="0" width="386" height="22" fill="url(#bStripeHot)"/>
    <rect class="stripe" x="386" y="0" width="386" height="22" fill="url(#bStripeCool)"/>

    <g class="brand-mark">
      <circle cx="386" cy="178" r="82" fill="none" stroke="#d9d9d9" stroke-width="4"/>
      <text class="mark-name" x="386" y="185" font-size="18" text-anchor="middle">BRENSDALE</text>
    </g>

    <text class="brand-title" x="386" y="313" font-size="40" text-anchor="middle" fill="url(#bSilver)">BRENSDALE ELECTRICAL</text>
    <text class="tagline" x="386" y="345" font-size="21" text-anchor="middle">professiona cost effective soloutions</text>
    <text class="tagline" x="386" y="372" font-size="21" text-anchor="middle">to all your electrical needs</text>

    <rect class="stripe" x="0" y="451" width="387" height="25" fill="url(#bStripeCoolRev)"/>
    <rect class="stripe" x="387" y="451" width="385" height="25" fill="url(#bStripeHotRev)"/>
  </svg>

</main>
</body>
</html>
```